Halvern Shipping

A flyer that sells both air and sea freight services. We had an attempt at this and wanted a fresh concept from your designers. Colors should be vibrant and the text readable on a digital billboard as well. Our attempt is attached along with our logo file.

Designers***The contents on our attempt flyer should be applied to your flyer design.

Thanks!

Industry/Entity Type

Shipping

```html
<!DOCTYPE html>
<html lang="en">
<head>
<meta charset="utf-8">
<title>Halvern Shipping – Save Money, Ship Better</title>
<link rel="stylesheet" href="https://fonts.googleapis.com/css2?family=Montserrat:wght@500;700;800;900&family=Roboto+Condensed:wght@400;700&display=swap">
<style>
  :root {
    --red: #c8202a;
    --red-deep: #7e0f14;
    --navy: #2b2f86;
    --sky: #3d9be6;
    --sky-light: #a9d4f5;
    --harbour-warm: #c9a25a;
    --hull-dark: #3a3a48;
    --white: #ffffff;
    --paper: #f3f3f3;
    --ink: #2a2a2a;
    --icon-dark: #2b2b2b;
    --backdrop: #e6e3de;
  }
  * { margin: 0; padding: 0; box-sizing: border-box; }
  html, body {
    width: 1200px; height: 900px; overflow: hidden;
    background: var(--backdrop);
  }
  .flyer {
    position: absolute; left: 297px; top: 20px;
    width: 606px; height: 860px;
    background: var(--paper);
    overflow: hidden;
    font-family: "Montserrat", sans-serif;
  }
  .flyer-top {
    position: absolute; left: 0; top: 0; width: 606px; height: 200px;
    background: var(--white);
  }
  .hero-photo {
    position: absolute; left: 0; top: 160px; width: 606px; height: 440px;
    background:
      radial-gradient(120% 70% at 0% 0%, rgba(255,255,255,1) 0%, rgba(255,255,255,0.95) 35%, rgba(255,255,255,0) 62%),
      radial-gradient(60% 40% at 45% 72%, rgba(58,58,72,0.55) 0%, rgba(58,58,72,0) 100%),
      radial-gradient(70% 35% at 30% 60%, rgba(201,162,90,0.45) 0%, rgba(201,162,90,0) 100%),
      linear-gradient(180deg, var(--sky) 0%, #6fb4ec 40%, var(--sky-light) 62%, #b7b3b8 76%, #c9504f 88%, var(--red) 100%);
  }
  .headline {
    position: absolute; left: 30px; top: 24px;
    font-weight: 900; font-size: 86px; line-height: 69px;
    letter-spacing: -1px;
  }
  .headline .line-red { color: var(--red); display: block; }
  .headline .line-navy { color: var(--navy); display: block; }
  .brand {
    position: absolute; left: 472px; top: 36px; width: 114px;
    text-align: center; color: var(--red);
    font-weight: 800;
  }
  .brand-mark {
    width: 68px; height: 68px; margin: 0 auto 6px;
    border: 4px solid var(--red); border-radius: 50%;
  }
  .brand-name { font-size: 22px; line-height: 22px; display: block; }
  .brand-sub { font-size: 15px; line-height: 18px; display: block; }
  .offer-panel {
    position: absolute; left: 0; top: 560px; width: 606px; height: 250px;
  }
  .offer-title {
    position: absolute; left: 46px; top: 582px;
    color: var(--white); font-weight: 700; font-size: 20px;
  }
  .services {
    position: absolute; top: 611px; list-style: none;
    color: var(--white); font-weight: 900; font-size: 20px; line-height: 29px;
  }
  .services.col-left { left: 48px; }
  .services.col-right { left: 296px; }
  .services li::before { content: "\2713"; font-weight: 500; margin-right: 7px; }
  .phone {
    position: absolute; left: 46px; top: 704px;
    display: flex; align-items: center; gap: 14px;
    color: var(--white); font-weight: 900; font-size: 62px; line-height: 70px; letter-spacing: 2px;
  }
  .social {
    position: absolute; top: 716px; width: 45px; height: 45px;
    background: var(--icon-dark); border-radius: 6px;
  }
  .social.first { left: 465px; }
  .social.second { left: 526px; }
  .footer {
    position: absolute; left: 20px; right: 20px; top: 802px;
    font-family: "Roboto Condensed", sans-serif; color: var(--ink);
    display: flex; justify-content: space-between; align-items: flex-end;
  }
  .signup { font-size: 14px; line-height: 20px; }
  .signup strong, .address { font-weight: 700; font-size: 14.5px; }
</style>
</head>
<body>
  <main class="flyer">
    <div class="flyer-top"></div>
    <div class="hero-photo" role="img" aria-label="Photo: a white passenger jet climbing through a blue sky above a container port, where a large black-and-red cargo ship is docked beside yellow gantry cranes and stacked containers — air and sea freight together"></div>

    <h1 class="headline">
      <span class="line-red">SAVE</span>
      <span class="line-red">MONEY</span>
      <span class="line-navy">SHIP</span>
      <span class="line-navy">BETTER</span>
    </h1>

    <div class="brand">
      <div class="brand-mark"></div>
      <span class="brand-name">HALVERN</span>
      <span class="brand-sub">shipping</span>
    </div>

    <svg class="offer-panel" viewBox="0 0 606 250" aria-hidden="true">
      <defs>
        <linearGradient id="panelFill" x1="0" y1="0" x2="0" y2="1">
          <stop offset="0" stop-color="#c8202a" stop-opacity="0"/>
          <stop offset="0.12" stop-color="#c8202a"/>
          <stop offset="0.7" stop-color="#b51a22"/>
          <stop offset="1" stop-color="#7e0f14"/>
        </linearGradient>
      </defs>
      <path d="M0 0 H606 V203 Q303 278 0 203 Z" fill="url(#panelFill)"/>
    </svg>

    <p class="offer-title">WE OFFER:</p>
    <ul class="services col-left">
      <li>CARGO</li>
      <li>CONSOLIDATION</li>
      <li>AIR FREIGHT</li>
    </ul>
    <ul class="services col-right">
      <li>SEA FREIGHT</li>
      <li>CUSTOMS CLEARANCE</li>
      <li>TRUCKING</li>
    </ul>

    <div class="phone">
      <svg width="42" height="42" viewBox="0 0 42 42" aria-hidden="true">
        <circle cx="21" cy="21" r="21" fill="#ffffff"/>
        <path d="M14 11 l5 0 l2 6 l-3 2 q3 6 8 8 l2 -3 l6 2 l0 5 q-1 2 -3 2 q-18 -2 -20 -19 q0 -2 3 -3 z" fill="#c8202a"/>
      </svg>
      <span>555-0142</span>
    </div>
    <div class="social first"></div>
    <div class="social second"></div>

    <footer class="footer">
      <p class="signup">Sign up to receive your suite#<br><strong>WWW.HALVERNSHIPPINGBAHAMAS.COM</strong></p>
      <p class="address"># 42 HARBOUR VIEW RD. NASSAU, BAHAMAS</p>
    </footer>
  </main>
</body>
</html>
```